ガソリンスタンド店頭での自動車保険の販売を考えています。
保険商品は情報の非対称性が高く、ほとんどの顧客が自身の補償内容をよく把握しいません。また販売方の十分な説明ができていないケースも多いです。そこでよくある補償のミスマッチの例を挙げて保険の見直しを促していきたいと考えています。具体的なミスマッチは以下の三点です。

①車両保険について
車両保険のは一般と限定の二種類がありますが限定では自損事故や当て逃げの際の費用は補償されません。これを理解していない顧客は多いです。

②弁護士費用
任意保険に未加入の自動車ユーザーは地域によってだいぶ変わりますが全体の4割程度います。任意保険未加入の自動車と事故を起こした場合相手に過失がある場合でも物損であれば泣き寝入りするしかありません。また人身事故の場合でも自賠責の補償範囲を超す部分については自腹で清算する必要があります。弁護士を立て相手方と交渉することはできますが莫大な費用がかかります。
弁護士費用特約に加入していればこうした状況を回避することができます。費用的にも数百円程度の付加保険料で済みます。

③運転者限定
実際に運転をする方を限定することで、また年齢条件を設定することにより保険料の減額が見込めます。
しかし保険の組み方が複雑なため補償が受けられない、また過剰な補償となっている場合が数多くあります。

保険は敬遠されがちな分野ですので固くなりすぎず、親しみやすい雰囲気のPOPにしてもらえたらと思います。またPOPの種類や形状等も同時に提案してもらえれば助かります。「加入するかはどうか置いといて無駄や不足があるといけませんので一度補償内容の見直しをされませんか?」というスタイルで販売活動を進めていきますのでそれに沿ったPOPを作って欲しいと思います。
上記①②③に対応した保険会社のパンフレットを添付します。参考にしてください。
補足です。
当社調べでは他社契約分について、適正な補償内容になっていない方は8割程度いらっしゃいました。見た方が自分は大丈夫だろうかと注意喚起出来るような内容にして欲しいと思います。
自体や雰囲気ですが全体的に堅い印象のデザインが多かったのでもう少しポップな感じ、親しみやすい感じにしてほしいです。
すいません、延期させて頂きます。
延長します。
延期します…

やわらかいタッチで、誰が見てもわかりやすい内容でした。

ありがとうございました。

来年より、活用させていただきます。

ご提案いただきありがとうございました。

```html
<!DOCTYPE html>
<html lang="ja">
<head>
<meta charset="utf-8">
<title>その保険、重くないですか？ 自動車保険見直しPOP</title>
<link rel="stylesheet" href="https://fonts.googleapis.com/css2?family=Noto+Sans+JP:wght@500;700;900&display=swap">
<style>
  :root {
    --paper: #ffffff;
    --ink: #1a1a1a;
    --band-red: #e60019;
    --band-text: #ffffff;
    --accent-blue: #1e8fd6;
    --visual-light: #e8d3b6;
    --visual-dark: #b58a5c;
  }
  * { margin: 0; padding: 0; box-sizing: border-box; }
  html, body {
    width: 849px;
    height: 1200px;
    overflow: hidden;
    background: var(--paper);
  }
  .pop {
    position: relative;
    width: 849px;
    height: 1200px;
    background: var(--paper);
    font-family: "Noto Sans JP", sans-serif;
    color: var(--ink);
    overflow: hidden;
  }
  .vertical {
    position: absolute;
    writing-mode: vertical-rl;
    text-orientation: upright;
    line-height: 1;
    white-space: nowrap;
  }

  /* left red band with checklist */
  .check-band {
    position: absolute;
    left: 133px;
    top: 0;
    width: 212px;
    height: 1200px;
    background: var(--band-red);
  }
  .check-band__lead {
    left: 283px;
    top: 70px;
    font-size: 46px;
    font-weight: 900;
    letter-spacing: 8px;
    color: var(--band-text);
  }
  .check-band__item {
    font-size: 30px;
    font-weight: 700;
    letter-spacing: 9px;
    color: var(--band-text);
    top: 200px;
  }
  .check-band__item--self  { left: 234px; }
  .check-band__item--legal { left: 183px; }
  .check-band__item--driver { left: 133px; left: 141px; }

  /* central visual */
  .carrier-visual {
    position: absolute;
    left: 360px;
    top: 40px;
    width: 220px;
    height: 1100px;
    border-radius: 16px;
    background: linear-gradient(180deg, var(--visual-light) 0%, var(--visual-dark) 70%, #3a3a3a 100%);
  }

  /* headline */
  .headline {
    font-weight: 900;
    font-size: 106px;
    letter-spacing: 4px;
    color: var(--ink);
  }
  .headline--first  { left: 697px; top: 50px; }
  .headline--second { left: 584px; top: 235px; }

  .subline {
    left: 734px;
    top: 670px;
    font-size: 32px;
    font-weight: 700;
    letter-spacing: 2px;
  }
  .product {
    left: 732px;
    top: 975px;
    font-size: 34px;
    font-weight: 900;
    letter-spacing: 3px;
    display: flex;
    align-items: center;
  }
  .product__dot {
    display: block;
    width: 26px;
    height: 26px;
    margin-top: 12px;
    border-radius: 50%;
    background: var(--accent-blue);
  }
</style>
</head>
<body>
  <main class="pop">
    <section class="check-band">
    </section>
    <h2 class="vertical check-band__lead">その保険は、</h2>
    <p class="vertical check-band__item check-band__item--self">自損事故、当て逃げの費用は　補償されますか？</p>
    <p class="vertical check-band__item check-band__item--legal">弁護士費用特約（数百円程度）　ご存じですか？</p>
    <p class="vertical check-band__item check-band__item--driver">運転者限定　年齢条件で保険料が減額されます。</p>

    <div class="carrier-visual" role="img" aria-label="「保険料減額」「運転者限定」「弁護士費用」「当て逃げ」「自損事故」と書かれた段ボール箱を高く積み上げて台車で運ぶ人物のイラスト"></div>

    <h1 class="vertical headline headline--first">その保険、</h1>
    <h1 class="vertical headline headline--second">重くないですか？</h1>

    <p class="vertical subline">無駄や不足を考える</p>
    <p class="vertical product">自動車保険<span class="product__dot"></span></p>
  </main>
</body>
</html>
```